Studying Effectively To Do List

I am looking to design a new "Study To Do List" for High School students (Ages 15 - 18) . This will be printed as an A4 notepad and so should only be a single A4 page.

The Design will need to be professional and look semi-serious but also be appealing to High school students (Ages 15 - 18) and should NOT be gender specific.

I have attached a word document outlining the structure of the page. The space provided should be large enough that people can write in it comfortably.

The notepad will most likely be printed in black and white but I'm also looking at coloured options - colours should be kept to a minimum.

This will be printed professionally and should also include a 3mm bleed.

The design should also include the business logo (included in the word document)

Target Market(s)

High School students (Ages 15 - 18). Both genders

Industry/Entity Type

Education

Font styles to use
Serif
Sans Serif

Requirements
Must have
• Please see the word document attached.
Should not have
• Too much colour

```html
<!DOCTYPE html>
<html lang="en">
<head>
<meta charset="utf-8">
<title>Study To Do List</title>
<link href="https://fonts.googleapis.com/css2?family=Exo+2:wght@500;700;800&display=swap" rel="stylesheet">
<style>
  :root {
    --orange: #f26a21;
    --ink: #8c8c8c;
    --ink-dark: #555555;
    --rule: #d6d6d6;
    --paper: #ffffff;
  }
  * { margin: 0; padding: 0; box-sizing: border-box; }
  html, body { width: 849px; height: 1200px; overflow: hidden; background: var(--paper); }
  body { font-family: "Exo 2", sans-serif; color: var(--ink); }

  .page { position: relative; width: 849px; height: 1200px; background: var(--paper); }

  .side-band { position: absolute; left: 0; top: 0; width: 85px; height: 1200px; background: var(--orange); }
  .edge-band { position: absolute; right: 0; top: 0; width: 19px; height: 1200px; background: var(--orange); }

  .side-label {
    position: absolute; left: 42px; transform: translate(-50%, -50%) rotate(-90deg);
    color: var(--paper); font-size: 13px; font-weight: 700; letter-spacing: 4px; white-space: nowrap;
  }

  .date { position: absolute; left: 118px; top: 58px; width: 330px; height: 36px; border-bottom: 1px solid var(--rule);
    font-size: 17px; font-weight: 700; letter-spacing: 5px; }

  .brand { position: absolute; left: 700px; top: 34px; display: flex; align-items: center; gap: 8px; }
  .brand-dot { width: 22px; height: 22px; border-radius: 50%; background: var(--orange); }
  .brand-name { font-size: 20px; font-weight: 800; color: var(--ink-dark); }

  .divider { position: absolute; left: 118px; width: 682px; height: 2px; background: var(--orange); }

  .rows { position: absolute; list-style: none; }
  .rows li { height: 28.5px; border-bottom: 1px solid var(--rule); display: flex; align-items: flex-end;
    padding-bottom: 4px; font-size: 11px; letter-spacing: 3px; position: relative; }
  .num { font-size: 12px; letter-spacing: 0; font-weight: 500; }
  .heading { font-weight: 500; font-size: 12px; }
  .sub { font-weight: 800; color: var(--ink-dark); font-size: 10px; letter-spacing: 2px; }
  .due { position: absolute; left: 440px; bottom: 4px; font-weight: 800; color: var(--ink-dark); font-size: 10px; }

  .practice { position: absolute; left: 467px; top: 1104px; transform: translate(-50%, -50%) rotate(-90deg);
    font-size: 12px; letter-spacing: 4px; font-weight: 500; white-space: nowrap; }
</style>
</head>
<body>
<main class="page">
  <div class="side-band"></div>
  <div class="edge-band"></div>

  <span class="side-label" style="top:160px">REVISION</span>
  <span class="side-label" style="top:430px">HOMEWORK</span>
  <span class="side-label" style="top:830px">ASSESSMENTS</span>
  <span class="side-label" style="top:1100px">NOTES</span>

  <div class="date">DATE</div>
  <div class="brand"><span class="brand-dot"></span><span class="brand-name">Northline</span></div>

  <ol class="rows" style="left:118px; top:100px; width:300px">
    <li class="num">1</li><li class="num">2</li><li class="num">3</li><li class="num">4</li>
  </ol>
  <ol class="rows" style="left:460px; top:100px; width:320px">
    <li class="num">5</li><li class="num">6</li><li class="num">7</li><li class="num">8</li>
  </ol>

  <div class="divider" style="top:250px"></div>

  <ul class="rows homework" style="left:118px; top:262px; width:682px">
    <li class="heading">SUBJECT</li><li class="sub">+ TASK</li>
    <li class="heading">SUBJECT</li><li class="sub">+ TASK</li>
    <li class="heading">SUBJECT</li><li class="sub">+ TASK</li>
    <li class="heading">SUBJECT</li><li class="sub">+ TASK</li>
    <li class="heading">SUBJECT</li><li class="sub">+ TASK</li>
    <li class="heading">SUBJECT</li><li class="sub">+ TASK</li>
  </ul>

  <div class="divider" style="top:645px"></div>

  <ul class="rows assessments" style="left:118px; top:653px; width:682px">
    <li class="heading">ASSESSMENT<span class="due">DUE</span></li><li class="sub">+ ELEMENT</li>
    <li class="heading">ASSESSMENT<span class="due">DUE</span></li><li class="sub">+ ELEMENT</li>
    <li class="heading">ASSESSMENT<span class="due">DUE</span></li><li class="sub">+ ELEMENT</li>
    <li class="heading">ASSESSMENT<span class="due">DUE</span></li><li class="sub">+ ELEMENT</li>
    <li class="heading">ASSESSMENT<span class="due">DUE</span></li><li class="sub">+ ELEMENT</li>
    <li class="heading">ASSESSMENT<span class="due">DUE</span></li><li class="sub">+ ELEMENT</li>
  </ul>

  <div class="divider" style="top:1024px"></div>

  <ol class="rows" style="left:118px; top:1040px; width:140px">
    <li class="num">1</li><li class="num">2</li><li class="num">3</li><li class="num">4</li>
  </ol>
  <ol class="rows" style="left:288px; top:1040px; width:150px">
    <li class="num">5</li><li class="num">6</li><li class="num">7</li><li class="num">8</li>
  </ol>
  <span class="practice">PRACTICE</span>
  <ul class="rows" style="left:500px; top:1040px; width:280px">
    <li></li><li></li><li></li><li></li>
  </ul>
</main>
</body>
</html>
```